Fun, Clean Business Card For Family Focused Travel Agency

I need a business card using specific colors and fonts as in the uploaded files. Ideally, I would like a large image of the logo on the back and all the contact info on the front. Maybe the stars/dots somewhere in a flowy form.

I do want it the contact information to be clear and easy to read. I don't want it to look too busy. Maybe even a bit minimalist.

I plan or ordering the ROUNDED CORNER business cards from Cardwell Press, so please consider that in your design.

Target Market(s)

Families with children, couples, groups of friends

Contact Information for Business Card

Marla Quent, Owner
Marla@TidewayTrips.example
Cell Phone Number 555-218-6034
Office Phone Number 555-647-1295
Specializing in Fablecrest destinations, Goldmere Parkside Resort, Cruises and All-Inclusive Vacations.

Nice but not required:
www.TidewayTrips.example
Facebook, Instagram, Twitter icons with username: TidewayTrips

Font styles to use
Sans Serif

Requirements
Must have
• Please try to use the colors from the logo as much as possible. I understand lighter shades/colors may be needed for some things.
Should not have
• NO SERIF FONTS. That is really the only thing I do not want at all

```html
<!DOCTYPE html>
<html lang="en">
<head>
<meta charset="utf-8">
<title>Tideway Trips – Business Card</title>
<link href="https://fonts.googleapis.com/css2?family=Ubuntu:ital,wght@0,400;0,500;0,700;1,400;1,500&display=swap" rel="stylesheet">
<style>
  :root{
    --teal:#13b195;
    --orange:#f7941d;
    --charcoal:#333333;
    --navy:#0d1b2a;
    --green:#8cc63f;
    --ink:#111111;
    --white:#ffffff;
    --backdrop:#1c1c1c;
  }
  *{margin:0;padding:0;box-sizing:border-box}
  html,body{width:1200px;height:1200px;overflow:hidden;background:var(--backdrop)}
  body{position:relative;font-family:"Ubuntu",sans-serif}
  .card{position:absolute;left:110px;width:980px;height:570px;border-radius:40px;overflow:hidden;background:var(--charcoal)}
  .card--front{top:20px}
  .card--back{top:610px}
  .card__shapes{position:absolute;inset:0;width:100%;height:100%}
  .right{position:absolute;right:66px;text-align:right;white-space:nowrap}
  .name{top:38px;font-size:60px;font-weight:500;letter-spacing:.5px}
  .name__first{color:var(--teal)}
  .name__last{color:var(--orange)}
  .role{top:104px;font-size:38px;font-weight:500;color:var(--orange)}
  .email{top:146px;font-size:21px;font-weight:500;color:var(--orange)}
  .phone{font-size:32px;font-weight:500;color:var(--ink);right:136px}
  .phone--office{top:182px}
  .phone--cell{top:237px}
  .phone-icon{position:absolute;right:58px;width:36px;height:36px;border-radius:50%}
  .phone-icon svg{width:36px;height:36px;display:block}
  .phone-icon--office{top:186px;background:var(--green)}
  .phone-icon--cell{top:241px;background:var(--orange)}
  .specialties{top:286px;font-size:25px;font-style:italic;font-weight:500;color:var(--teal);line-height:36px}
  .social{position:absolute;top:410px;right:60px;display:flex;align-items:center;gap:14px}
  .social__handle{font-size:21px;font-weight:500;color:var(--orange);margin-right:8px}
  .social__dot{width:30px;height:30px;border-radius:6px}
  .social__dot--a{background:#55acee}
  .social__dot--b{background:#e1306c}
  .social__dot--c{background:#3b5998}
  .website{top:516px;font-size:27px;color:var(--teal)}
  .watermark{position:absolute;left:290px;top:300px;font-size:120px;font-weight:700;color:var(--charcoal);opacity:.06;white-space:nowrap}
  .corner-mark{position:absolute;left:26px;top:494px;display:flex;align-items:center;gap:8px;color:var(--white);font-size:24px;font-weight:700;white-space:nowrap}
  .corner-mark__dot{width:28px;height:28px;border-radius:50%;background:var(--white);flex:none}
  .brand{position:absolute;left:410px;top:110px;width:550px;display:flex;align-items:center;justify-content:center;gap:18px;white-space:nowrap}
  .brand__dot{width:100px;height:100px;border-radius:50%;background:var(--teal);flex:none}
  .brand__name{font-size:56px;font-weight:700;color:var(--navy);line-height:1}
  .brand-url{position:absolute;left:410px;width:550px;top:244px;text-align:center;font-size:27px;font-weight:500;color:var(--teal)}
  .social--back{top:515px}
</style>
</head>
<body>

<section class="card card--front" aria-label="Business card front">
  <svg class="card__shapes" viewBox="0 0 980 570" preserveAspectRatio="none" aria-hidden="true">
    <rect width="980" height="570" fill="var(--charcoal)"/>
    <path d="M30 0 L470 0 C300 80 170 190 130 320 C95 200 60 90 30 0Z" fill="var(--teal)"/>
    <path d="M460 0 L980 0 L980 570 L520 570 C230 520 90 360 130 300 C180 190 300 80 460 0Z" fill="var(--white)"/>
  </svg>
  <div class="watermark" aria-hidden="true">Tideway</div>

  <h1 class="right name"><span class="name__first">Marla</span> <span class="name__last">Quent</span></h1>
  <p class="right role">Owner</p>
  <p class="right email">Marla@TidewayTrips.example</p>

  <p class="right phone phone--office">555.647.1295</p>
  <span class="phone-icon phone-icon--office" aria-label="Office phone">
    <svg viewBox="0 0 36 36"><path d="M12 9c1 0 2 3 2.5 4.5.3 1-1.5 2-1.5 2.5 1 2.5 3.5 5 6 6 .5 0 1.5-1.8 2.5-1.5 1.5.5 4.5 1.5 4.5 2.5 0 1.5-2 4-4 4C14 27 9 22 9 13c0-2 2-4 3-4z" fill="#fff"/></svg>
  </span>
  <p class="right phone phone--cell">555.218.6034</p>
  <span class="phone-icon phone-icon--cell" aria-label="Cell phone">
    <svg viewBox="0 0 36 36"><rect x="12" y="8" width="12" height="20" rx="2" fill="#fff"/><rect x="14" y="11" width="8" height="12" fill="var(--orange)"/></svg>
  </span>

  <p class="right specialties">Specializing in Fablecrest destinations,<br>Goldmere Parkside Resort, Cruises<br>and All-Inclusive Vacations.</p>

  <div class="social">
    <span class="social__handle">TidewayTrips</span>
    <span class="social__dot social__dot--a" aria-hidden="true"></span>
    <span class="social__dot social__dot--b" aria-hidden="true"></span>
    <span class="social__dot social__dot--c" aria-hidden="true"></span>
  </div>

  <p class="right website">www.TidewayTrips.example</p>

  <div class="corner-mark"><span class="corner-mark__dot" aria-hidden="true"></span>Tideway Trips</div>
</section>

<section class="card card--back" aria-label="Business card back">
  <svg class="card__shapes" viewBox="0 0 980 570" preserveAspectRatio="none" aria-hidden="true">
    <rect width="980" height="570" fill="var(--charcoal)"/>
    <path d="M30 0 L470 0 C300 80 170 190 130 320 C95 200 60 90 30 0Z" fill="var(--teal)"/>
    <path d="M460 0 L980 0 L980 570 L520 570 C230 520 90 360 130 300 C180 190 300 80 460 0Z" fill="var(--white)"/>
  </svg>

  <div class="brand">
    <span class="brand__dot" aria-hidden="true"></span>
    <span class="brand__name">Tideway Trips</span>
  </div>
  <p class="brand-url">www.TidewayTrips.example</p>

  <div class="social social--back">
    <span class="social__handle">TidewayTrips</span>
    <span class="social__dot social__dot--a" aria-hidden="true"></span>
    <span class="social__dot social__dot--b" aria-hidden="true"></span>
    <span class="social__dot social__dot--c" aria-hidden="true"></span>
  </div>

  <div class="corner-mark"><span class="corner-mark__dot" aria-hidden="true"></span>Tideway Trips</div>
</section>

</body>
</html>
```